CALM.OTTER snowsport and living

Calm Otter webpage design brief

Calm Otter is a life style brand
for those who love winter, snowboarding, and coffee.

We have log houses at some best snowboarding locations in Japan, in which easy and comfortable ambience make guests feel at home during their winter stay. Out there on the slopes, there are Calm Otter’s exclusive coffee kiosks that offer a wide selection of fine coffee from boutique roasters over the world to warm the hands and hearts of whenever our guests need!

Enjoy the snow with Calm Otter!

Tone & Manner: Simple, Tranquil, Relaxed, Enjoyable
 
Look and Feel : Monotone images of log house in the snowy winter and snowboarding people.  Capture of real-people-real-life moments. Red and blue colors can be used on icons and other vector elements in a much smaller scale in the overall picture.  Please refer to the attached color pallette.

Mainly informational with links to Stayvorn for booking
Social media registration pass over from talkloop. pagemural or Stayvorn
Recruitment link to Jobvane

Currently I do not have any pictures. So need a bit of discussion on this area.

Also the website needs to be in 3 languages, English, Chinese and Japanese.

Rough Sitemap:

Home (language selection on every page)
About
GO (snow villas)
Coffee (coffee kiosks on slopes)
Reservations

(Bottom of screen)
Contact us
Company info
Recruit

Reference website:
Quillbrook.example
Mossgate.example.jp

Attached pictures are for references not for use!!!
Color reference pls refer to attached file 4.

Reason: More updates on project briefs. Please have a look.

Target Market(s)

Snowboarders

Industry/Entity Type

Hospitality

Number of Pages Required

5+ page

Font styles to use
Sans Serif

Colors

Designer to choose colors to be used in the design.

Requirements
Must have
• Mobile version
• 3 languages
• Registration thru TalkLoop, Pagemural or Stayvorn
Nice to have
• Illustration instead of pictures

```html
<!DOCTYPE html>
<html lang="en">
<head>
<meta charset="utf-8">
<title>Calm Otter – Snowsport and Living</title>
<link href="https://fonts.googleapis.com/css2?family=Comic+Neue:wght@400;700&display=swap" rel="stylesheet">
<style>
:root{
  --cyan:#43d8e3;
  --brand-red:#a33a28;
  --btn-red:#9b2a2a;
  --black:#111111;
  --teal:#1f7f86;
  --footer:#484444;
  --white:#ffffff;
  --ink:#1c1c1c;
}
*{margin:0;padding:0;box-sizing:border-box}
html,body{width:1200px;height:1200px;overflow:hidden;background:var(--white)}
body{font-family:"Comic Neue",sans-serif;color:var(--ink)}
.page{position:absolute;left:274px;top:0;width:651px;height:1200px;background:var(--white);overflow:hidden}
.abs{position:absolute}

/* header */
.site-header{left:0;top:0;width:651px;height:61px;background:var(--cyan)}
.brand{left:46px;top:11px;color:var(--brand-red);font-weight:700}
.brand-name{font-size:21px;letter-spacing:1px;line-height:1}
.brand-tag{font-size:9px;letter-spacing:.5px;margin-top:4px}
.contact-item{top:20px;font-size:9.5px;display:flex;align-items:center;gap:4px;color:var(--ink);white-space:nowrap}
.search{left:451px;top:19px;width:105px;height:17px;background:var(--white);display:flex;justify-content:flex-end;align-items:center;padding-right:4px}
.lang{left:564px;top:19px;width:40px;height:17px;background:var(--white);font-size:8px;display:flex;align-items:center;justify-content:center}

/* nav */
.main-nav{left:0;top:61px;width:651px;height:35px;background:var(--black)}
.main-nav a{position:absolute;top:13px;color:var(--white);font-size:8.5px;font-weight:700;text-decoration:none;letter-spacing:.3px}

/* hero */
.hero{left:0;top:96px;width:651px;height:296px;background:linear-gradient(160deg,#5b5f6e 0%,#7d8090 40%,#9a9ca8 65%,#6a6c78 100%)}
.hero-line{left:0;top:392px;width:651px;height:2px;background:var(--cyan)}
.hero-title{left:0;top:170px;width:651px;text-align:center;color:var(--white);font-size:18px;font-weight:700;letter-spacing:1px}
.field{height:18px;background:var(--cyan);font-size:9px;font-weight:700;display:flex;align-items:center;justify-content:space-between;padding:0 4px 0 5px}
.check-btn{left:280px;top:283px;width:80px;height:27px;background:var(--btn-red);color:var(--white);font-size:7.5px;font-weight:700;display:flex;align-items:center;justify-content:center}

.photo{box-shadow:0 2px 4px rgba(0,0,0,.45)}
.caption{font-size:7.5px;line-height:10.5px;width:258px}

/* dark band */
.feature-band{left:0;top:555px;width:651px;height:249px;background:linear-gradient(100deg,#44555b 0%,#3b4c52 50%,#4e6068 100%)}
.band-title{width:651px;left:0;text-align:center;color:var(--white);font-size:14px;font-weight:700;letter-spacing:.5px}
.band-text{color:var(--white);font-size:7.5px;line-height:11.5px;text-align:center}

/* accommodation */
.section-label{left:46px;top:818px;color:var(--teal);font-size:11.5px;font-weight:700;letter-spacing:.5px}
.tab{top:842px;height:24px;width:93px;background:var(--cyan);font-size:11px;padding-left:10px;display:flex;align-items:center;color:#22575c}
.villa-title{left:46px;top:887px;font-size:13.5px;font-weight:700}
.villa-text{left:46px;top:915px;width:342px;font-size:8.8px;line-height:16px}

/* footer */
.site-footer{left:0;top:1049px;width:651px;height:125px;background:var(--footer)}
.foot-title{top:1064px;color:var(--cyan);font-size:9.5px;font-weight:700;letter-spacing:.4px}
.foot-text{top:1082px;color:var(--white);font-size:6.2px;line-height:10.5px;text-align:justify}
.read-more{left:182px;top:1144px;color:var(--cyan);font-size:7.5px;font-weight:700}
.input{left:264px;width:139px;height:16px;background:var(--white);border:1px solid #999}
.send{left:264px;top:1132px;width:68px;height:22px;background:var(--cyan);font-size:8px;font-weight:700;display:flex;align-items:center;justify-content:center;border:1px solid var(--white)}
.bottom-bar{left:0;top:1174px;width:651px;height:26px;background:var(--black);color:var(--white);font-size:7px;display:flex;align-items:center;justify-content:center}
</style>
</head>
<body>
<div class="page">

  <header class="site-header abs">
    <div class="brand abs">
      <div class="brand-name">CALM OTTER</div>
      <div class="brand-tag">SNOWSPORT AND LIVING</div>
    </div>
    <div class="contact-item abs" style="left:214px">
      <svg width="10" height="12" viewBox="0 0 10 12"><path d="M2 0.5 L4 3 L3 4.5 Q4 7.5 6 9 L7.5 8 L9.7 10.2 L8 11.7 Q3 10 0.6 2.5 Z" fill="#222"/></svg>
      040-555-010-203
    </div>
    <div class="contact-item abs" style="left:322px">
      <svg width="13" height="10" viewBox="0 0 13 10"><rect x="0.7" y="0.7" width="11.6" height="8.6" fill="none" stroke="#222" stroke-width="1.2"/><path d="M0.7 0.7 L6.5 5.5 L12.3 0.7" fill="none" stroke="#222" stroke-width="1.2"/></svg>
      mail@calmotter.example
    </div>
    <div class="search abs">
      <svg width="10" height="10" viewBox="0 0 10 10"><circle cx="4" cy="4" r="3" fill="none" stroke="#111" stroke-width="1.5"/><path d="M6.2 6.2 L9.3 9.3" stroke="#111" stroke-width="1.7"/></svg>
    </div>
    <div class="lang abs">English</div>
  </header>

  <nav class="main-nav abs">
    <a href="#" style="left:50px">HOME</a>
    <a href="#" style="left:106px">ABOUT</a>
    <a href="#" style="left:166px">GO</a>
    <a href="#" style="left:209px">COFFEE</a>
    <a href="#" style="left:271px">RESERVATIONS</a>
  </nav>

  <section class="hero abs" role="img" aria-label="Snowy ski slope with chairlift and two skiers, darkened"></section>
  <div class="hero-line abs"></div>
  <h1 class="hero-title abs">BOOK YOUR ACCOMMODATION ONLINE NOW !</h1>
  <div class="field abs" style="left:152px;top:218px;width:163px">ARRIVALS
    <svg width="12" height="11" viewBox="0 0 12 11"><rect x="0.6" y="1.2" width="10.8" height="9.2" fill="none" stroke="#333"/><rect x="0.6" y="1.2" width="10.8" height="2.3" fill="#333"/><path d="M2 5h1.5M5 5h1.5M8 5h1.5M2 7h1.5M5 7h1.5M8 7h1.5M2 9h1.5M5 9h1.5" stroke="#333"/></svg>
  </div>
  <div class="field abs" style="left:333px;top:218px;width:163px">DEPARTURE
    <svg width="12" height="11" viewBox="0 0 12 11"><rect x="0.6" y="1.2" width="10.8" height="9.2" fill="none" stroke="#333"/><rect x="0.6" y="1.2" width="10.8" height="2.3" fill="#333"/><path d="M2 5h1.5M5 5h1.5M8 5h1.5M2 7h1.5M5 7h1.5M8 7h1.5M2 9h1.5M5 9h1.5" stroke="#333"/></svg>
  </div>
  <div class="field abs" style="left:238px;top:248px;width:164px">NO OF PERSONS
    <svg width="8" height="6" viewBox="0 0 8 6"><path d="M1 1 L4 4.5 L7 1" fill="none" stroke="#111" stroke-width="1.6"/></svg>
  </div>
  <div class="check-btn abs">CHECK NOW</div>

  <div class="photo abs" style="left:44px;top:338px;width:266px;height:164px;background:linear-gradient(135deg,#8a5a32,#c48a4c 45%,#6a4226)" role="img" aria-label="Snowboarder in blue jacket reading inside a wooden cabin"></div>
  <div class="photo abs" style="left:338px;top:338px;width:266px;height:164px;background:linear-gradient(180deg,#b9bcc0 0%,#8e8a86 45%,#e8e8ea 70%,#f2f2f2 100%)" role="img" aria-label="Log house surrounded by snowy trees in winter"></div>
  <p class="caption abs" style="left:46px;top:510px">Lorem Ipsum is simply dummy text of the printing and typesetting industry. Lorem Ipsum has been the industry's standard dummy text ever since the 1500s</p>
  <p class="caption abs" style="left:338px;top:510px">Lorem Ipsum is simply dummy text of the printing and typesetting industry. Lorem Ipsum has been the industry's standard dummy text ever since the 1500s</p>

  <section class="feature-band abs" role="img" aria-label="Person enjoying coffee at a slope kiosk, darkened teal tone"></section>
  <h2 class="band-title abs" style="top:569px">SNOW VILLAS</h2>
  <p class="band-text abs" style="left:180px;top:603px;width:334px">Lorem Ipsum is simply dummy text of the printing and typesetting industry. Lorem Ipsum has been the industry's standard dummy text ever since the 1500s, when an unknown printer took a galley of type and scrambled it to make a type specimen book. It has survived not only five centuries, but also the leap into electronic typesetting, remaining essentially unchanged.</p>
  <h2 class="band-title abs" style="top:676px">COFFEE KIOSKS ON SLOPES</h2>
  <p class="band-text abs" style="left:196px;top:711px;width:270px">Lorem Ipsum is simply dummy text of the printing and typesetting industry. Lorem Ipsum has been the industry's standard dummy text ever since the 1500s, when an unknown printer took a galley of type and scrambled it to make a type specimen book. It has survived not only five centuries, but also the leap into electronic typesetting, remaining essentially unchanged.</p>

  <div class="section-label abs">Accommodation</div>
  <div class="tab abs" style="left:44px">Description</div>
  <div class="tab abs" style="left:139px">Price</div>
  <div class="tab abs" style="left:234px">Guests</div>
  <div class="tab abs" style="left:330px">Others</div>

  <h3 class="villa-title abs">Powder Drift Inn Villas</h3>
  <p class="villa-text abs">Lorem Ipsum is simply dummy text of the printing and typesetting industry. Lorem Ipsum has been the industry's standard dummy text ever since the 1500s, when an unknown printer took a galley of type and scrambled it to make a type specimen book.</p>
  <div class="photo abs" style="left:396px;top:882px;width:208px;height:139px;background:linear-gradient(180deg,#6f7d70 0%,#a9b2aa 40%,#e6e8e8 70%,#d9dcdc 100%)" role="img" aria-label="Red pickup truck parked in a snowy pine forest"></div>

  <footer class="site-footer abs"></footer>
  <h4 class="foot-title abs" style="left:46px">COMPANY INFO</h4>
  <p class="foot-text abs" style="left:46px;width:184px">It is a long established fact that a reader will be distracted by the readable content of a page when looking at its layout. The point of using Lorem Ipsum is that it has a more-or-less normal distribution of letters, as opposed to using 'Content here, content here', making it look like readable English.</p>
  <div class="read-more abs">READ MORE</div>
  <h4 class="foot-title abs" style="left:263px">CONTACT US</h4>
  <div class="input abs" style="top:1086px"></div>
  <div class="input abs" style="top:1107px"></div>
  <div class="send abs">SEND</div>
  <h4 class="foot-title abs" style="left:420px">RECRUITMENT</h4>
  <p class="foot-text abs" style="left:420px;width:184px">The point of using Lorem Ipsum is that it has a more-or-less normal distribution of letters, as opposed to using 'Content here, content here', making it look like readable English.</p>
  <div class="bottom-bar abs">Copy Rights Reserved ©2017 Calm Otter Snowsport And Living</div>

</div>
</body>
</html>
```